Now Open Poster

We need a banner for our sports supplement and nutritional store, Harbor Nutrition.
We were hoping for some sort of creative word art piece.
I have drawn my own mock up just to give you all a very basic starting point. But you are free to go with whatever you feel will work best.
The primary objective is simply to explain a little about what the company does, and then direct traffic towards the store with an 'Open Arrow' pointing left.
Text words we have chosen are:
Protein
Creatine
Health
Fitness
Sports Science
Nutrition
Energy
Achievement
Amino Acids
Organic
Supplements
Performance
Testosterone Support
Vitamins
Growth
Diet
Happiness
Weight Loss
Strong
Natural
Vitality
Accomplished
Below the word art we want our logo (See attached options)
Then below the logo the phrase "Success Starts Here"
Dimensions of the poster are 140cm x 60cm.
Colours: Blues/Whites/Greys/Blacks (Lots of white space please)
Here are some cool pieces I found that had some interesting elements that I liked (I'd love to see a mash-up of styles with a street art feel to it. Something funky!):
http://www.moodgrove.example/pin/804417263190552871/
http://www.moodgrove.example/pin/615380924471208539/
http://www.moodgrove.example/pin/804417263192736155/
http://www.moodgrove.example/pin/804417263194418620/
http://www.moodgrove.example/pin/937162048856301742/
Thanks for reading, message me if you have any further questions!
- Tobias

```html
<!DOCTYPE html>
<html lang="en">
<head>
<meta charset="utf-8">
<title>Harbor Nutrition – Now Open</title>
<link rel="stylesheet" href="https://fonts.googleapis.com/css2?family=Orbitron:wght@500;600;700&display=swap">
<style>
  :root {
    --ice-light: #f3f8fd;
    --ice-mid: #d6e6f4;
    --ice-deep: #b9d2ea;
    --word-blue: #2a78c2;
    --word-grey: #54595e;
    --ink: #0d0d0d;
  }
  html, body {
    margin: 0;
    padding: 0;
    overflow: hidden;
  }
  .poster {
    position: relative;
    width: 1200px;
    height: 2800px;
    overflow: hidden;
    background: var(--ice-light);
  }
  .poster-art {
    display: block;
    width: 1200px;
    height: 2800px;
  }
  .word-art text,
  .open-label,
  .slogan,
  .brand-name {
    font-family: "Orbitron", sans-serif;
  }
  .word-art text { font-size: 96px; font-weight: 600; }
  .word-art .blue { fill: var(--word-blue); }
  .word-art .grey { fill: var(--word-grey); }
  .open-label { font-size: 150px; font-weight: 700; fill: var(--ink); }
  .open-arrow-line { stroke: var(--ink); stroke-width: 10; }
  .open-arrow-head { fill: var(--ink); }
  .slogan { font-size: 100px; font-weight: 600; fill: var(--ink); }
  .logo-ring { fill: none; stroke: var(--ink); stroke-width: 6; }
  .brand-name { font-size: 58px; font-weight: 700; fill: var(--ink); }
</style>
</head>
<body>
<main class="poster">
  <svg class="poster-art" viewBox="0 0 1200 2800" xmlns="http://www.w3.org/2000/svg">
    <defs>
      <linearGradient id="ice-wash" x1="0" y1="0" x2="1" y2="1">
        <stop offset="0" stop-color="#d6e6f4"/>
        <stop offset="0.45" stop-color="#f3f8fd"/>
        <stop offset="0.75" stop-color="#b9d2ea"/>
        <stop offset="1" stop-color="#f3f8fd"/>
      </linearGradient>
    </defs>

    <rect class="ice-backdrop" x="0" y="0" width="1200" height="2800" fill="url(#ice-wash)"
          role="img" aria-label="Pale blue icy watercolour texture background"/>

    <g class="open-sign">
      <text class="open-label" x="675" y="138" textLength="500" lengthAdjust="spacingAndGlyphs">OPEN</text>
      <line class="open-arrow-line" x1="360" y1="170" x2="1175" y2="170"/>
      <polygon class="open-arrow-head" points="320,170 380,135 370,170 380,205"/>
    </g>

    <g class="word-art">
      <text class="blue" x="137" y="385" textLength="937" lengthAdjust="spacingAndGlyphs">Protein Creatine</text>
      <text class="blue" x="175" y="510" textLength="850" lengthAdjust="spacingAndGlyphs">Health Fitness</text>
      <text class="blue" x="162" y="635" textLength="888" lengthAdjust="spacingAndGlyphs">Sports Science</text>
      <text class="grey" x="225" y="760" textLength="755" lengthAdjust="spacingAndGlyphs">I AM BETTER</text>
      <text class="grey" x="150" y="885" textLength="913" lengthAdjust="spacingAndGlyphs">THAN YESTER-</text>
      <text class="grey" x="478" y="1010" textLength="250" lengthAdjust="spacingAndGlyphs">DAY</text>
      <text class="blue" x="137" y="1135" textLength="933" lengthAdjust="spacingAndGlyphs">Nutrition Energy</text>
      <text class="blue" x="225" y="1260" textLength="750" lengthAdjust="spacingAndGlyphs">Supplements</text>
      <text class="blue" x="225" y="1385" textLength="755" lengthAdjust="spacingAndGlyphs">Performance</text>
      <text class="blue" x="212" y="1510" textLength="780" lengthAdjust="spacingAndGlyphs">Testosterone</text>
      <text class="blue" x="125" y="1635" textLength="965" lengthAdjust="spacingAndGlyphs">Vitamins Growth</text>
      <text class="grey" x="175" y="1760" textLength="855" lengthAdjust="spacingAndGlyphs">Diet Happiness</text>
      <text class="grey" x="175" y="1885" textLength="855" lengthAdjust="spacingAndGlyphs">Strong Natural</text>
      <text class="grey" x="200" y="2010" textLength="805" lengthAdjust="spacingAndGlyphs">Accomplished</text>
    </g>

    <g class="brand-badge">
      <circle class="logo-ring" cx="600" cy="2380" r="285"/>
      <text class="brand-name" text-anchor="middle">
        <tspan x="600" y="2365">HARBOR</tspan>
        <tspan x="600" y="2440">NUTRITION</tspan>
      </text>
    </g>

    <text class="slogan" x="137" y="2775" textLength="938" lengthAdjust="spacingAndGlyphs">I AM STRONGER</text>
  </svg>
</main>
</body>
</html>
```